Film and TV production company

I have the logo already designed by mark quarry. I just need the text and the logo attached to the business card. Maybe a small design on the back of the card or text.

Industry/Entity Type

film tv arts

Contact Information for Business Card

Dale Morrow Cinematographer-Director

Colors
F0912C
F2A743
F7CA91
FBE8D2
FDF5EE
EE7325
F08F49
F5BC92
FAE3D3
FDF4ED

Requirements
Must have
• www.copperlanepix.com.au my email address mail@copperlanepix.com.au my mobile number 0491570158
Nice to have
• Some kind of small art work on the back that ties in with the logo design attached
Should not have
• Must clean and simple

```html
<!DOCTYPE html>
<html lang="en">
<head>
<meta charset="UTF-8">
<title>Copper Lane Pix — Business Card</title>
<link rel="stylesheet" href="https://fonts.googleapis.com/css2?family=Playfair+Display:wght@700&family=Lato:wght@400&display=swap">
<style>
  :root {
    --card-black: #000000;
    --gold: #E6C188;
    --gold-soft: rgba(230, 193, 136, 0.28);
    --gold-fade: rgba(230, 193, 136, 0);
    --sun-orange: #E8821A;
  }

  html, body {
    margin: 0;
    padding: 0;
    width: 1200px;
    height: 706px;
    overflow: hidden;
    background: var(--card-black);
  }

  .card {
    position: relative;
    width: 1200px;
    height: 706px;
    background: var(--card-black);
    overflow: hidden;
  }

  .corner-ornament {
    position: absolute;
    width: 296px;
    height: 274px;
  }
  .corner-ornament--top-left {
    left: 0; top: 0;
    background: radial-gradient(ellipse at 0% 0%, var(--gold-soft) 0%, var(--gold-fade) 72%);
  }
  .corner-ornament--top-right {
    right: 0; top: 0;
    background: radial-gradient(ellipse at 100% 0%, var(--gold-soft) 0%, var(--gold-fade) 72%);
  }
  .corner-ornament--bottom-left {
    left: 0; bottom: 0;
    background: radial-gradient(ellipse at 0% 100%, var(--gold-soft) 0%, var(--gold-fade) 72%);
  }
  .corner-ornament--bottom-right {
    right: 0; bottom: 0;
    background: radial-gradient(ellipse at 100% 100%, var(--gold-soft) 0%, var(--gold-fade) 72%);
  }

  .brand-mark {
    position: absolute;
    left: 519px;
    top: 135px;
    width: 162px;
    height: 162px;
  }

  .brand-name {
    position: absolute;
    left: 0;
    width: 100%;
    top: 326px;
    margin: 0;
    text-align: center;
    font-family: "Playfair Display", Georgia, serif;
    font-weight: 700;
    font-size: 70px;
    line-height: 1;
    letter-spacing: 0.01em;
    color: var(--gold);
  }

  .brand-region {
    position: absolute;
    left: 0;
    width: 100%;
    top: 428px;
    margin: 0;
    text-align: center;
    font-family: "Lato", Arial, sans-serif;
    font-weight: 400;
    font-size: 35px;
    line-height: 1;
    letter-spacing: 0.22em;
    text-indent: 0.22em;
    color: var(--gold);
  }
</style>
</head>
<body>
  <main class="card">
    <div class="corner-ornament corner-ornament--top-left" role="img" aria-label="Gold line-art geometric star pattern in the top-left corner"></div>
    <div class="corner-ornament corner-ornament--top-right" role="img" aria-label="Gold line-art geometric star pattern in the top-right corner"></div>
    <div class="corner-ornament corner-ornament--bottom-left" role="img" aria-label="Gold line-art geometric star pattern in the bottom-left corner"></div>
    <div class="corner-ornament corner-ornament--bottom-right" role="img" aria-label="Gold line-art geometric star pattern in the bottom-right corner"></div>

    <svg class="brand-mark" viewBox="0 0 162 162" aria-hidden="true">
      <circle cx="81" cy="81" r="81" fill="var(--sun-orange)"/>
    </svg>

    <h1 class="brand-name">COPPER LANE PIX</h1>
    <p class="brand-region">AUSTRALIA</p>
  </main>
</body>
</html>
```